marcel's mobile mechanic

a business card that will get attention from clients
- name of the business: M'S MOBILE MECHANIC
- we currently do not have a logo and do not need one at the moment, happy for the designers to just put the business name on the card using appropriate fonts

Target Market(s)

low cost mobile repairs

Industry/Entity Type

Business

Contact Information for Business Card

attracts customers

Font styles to use
Sans Serif

Colors
0255a3
fbee3d
000000

Requirements
Must have
• (555) 318-4907
• Marcel Treviño
• for lower income target market
Nice to have
• "we save you money"
• Easy to read
Should not have
• nothing comes to mind

```html
<!DOCTYPE html>
<html lang="en">
<head>
<meta charset="utf-8">
<title>M'S Mobile Mechanic – Business Card</title>
<link href="https://fonts.googleapis.com/css2?family=Roboto:ital,wght@0,400;0,500;1,400&family=Noto+Serif:ital@1&display=swap" rel="stylesheet">
<style>
  :root {
    --stage: #1a1a1a;
    --brand-blue: #004b8d;
    --brand-yellow: #f8c400;
    --paper: #f9f9f9;
    --ink: #3d4043;
    --ink-soft: #555a5e;
  }
  * { box-sizing: border-box; margin: 0; padding: 0; }
  html, body {
    width: 1200px; height: 647px; overflow: hidden;
    background: var(--stage);
  }
  .stage { position: relative; width: 1200px; height: 647px; }
  .card {
    position: absolute; top: 182px; width: 466px; height: 281px;
    overflow: hidden;
  }
  .card-front { left: 115px; background: var(--brand-blue); }
  .card-back { left: 618px; background: var(--paper); }

  .business-name {
    position: absolute;
    font-family: "Roboto", sans-serif;
    font-weight: 500;
    letter-spacing: 0.5px;
    white-space: nowrap;
    line-height: 1;
  }
  .card-front .business-name {
    left: 0; right: 0; top: 116px; text-align: center;
    font-size: 28px; color: #fff;
  }
  .card-back .business-name {
    left: 26px; top: 66px; font-size: 24px; color: var(--ink);
  }

  .tagline-front {
    position: absolute; left: 43px; right: 41px; top: 249px;
    display: flex; align-items: center; justify-content: space-between;
    font-family: "Roboto", sans-serif; font-size: 12px; color: #fff;
  }
  .tagline-front .rule {
    width: 91px; height: 3px; background: var(--brand-yellow);
  }
  .tagline-front .rule.left { clip-path: polygon(0 50%, 100% 0, 100% 100%); }
  .tagline-front .rule.right { clip-path: polygon(0 0, 100% 50%, 0 100%); }

  .person { position: absolute; left: 26px; top: 182px; font-family: "Roboto", sans-serif; }
  .person-name { font-size: 18px; color: var(--brand-blue); font-weight: 400; line-height: 1.1; }
  .person-title { font-size: 11px; font-style: italic; color: var(--ink-soft); margin-top: 4px; }

  .contacts {
    position: absolute; left: 239px; top: 166px; list-style: none;
    font-family: "Roboto", sans-serif; font-size: 12px; color: var(--ink-soft);
  }
  .contacts li { display: flex; align-items: center; height: 16.5px; }
  .contacts svg { width: 9px; height: 9px; margin-right: 8px; fill: var(--brand-blue); }

  .footer-band { position: absolute; inset: 0; }
  .tagline-back {
    position: absolute; left: 234px; top: 255px;
    font-family: "Noto Serif", serif; font-style: italic; font-size: 11px; color: #fff;
  }
</style>
</head>
<body>
<main class="stage">
  <section class="card card-front">
    <h1 class="business-name">M'S MOBILE MECHANIC</h1>
    <p class="tagline-front"><span class="rule left"></span>for lower income target market<span class="rule right"></span></p>
  </section>

  <section class="card card-back">
    <h2 class="business-name">M'S MOBILE MECHANIC</h2>

    <div class="person">
      <p class="person-name">Marcel Treviño</p>
      <p class="person-title">Vice President</p>
    </div>

    <ul class="contacts">
      <li><svg viewBox="0 0 10 10"><path d="M1 3.5C1 2 2.5 1 5 1s4 1 4 2.5L7.5 4 7 3H3L2.5 4zM2.5 4.5h5L9 9H1z"/></svg>(555) 318-4907</li>
      <li><svg viewBox="0 0 10 10"><path d="M0 2h10v1L5 6 0 3zM0 4l5 3 5-3v4H0z"/></svg>marcel@msmobilemechanic.com</li>
      <li><svg viewBox="0 0 10 10"><circle cx="5" cy="5" r="4.3" fill="none" stroke="var(--brand-blue)" stroke-width="1.2"/><path d="M0.8 5h8.4M5 0.8v8.4" stroke="var(--brand-blue)" stroke-width="1"/></svg>www.msmobilemechanic.com</li>
    </ul>

    <svg class="footer-band" width="466" height="281" aria-hidden="true">
      <rect x="0" y="263" width="205" height="18" fill="var(--brand-yellow)"/>
      <polygon points="202,245 466,245 466,281 188,281" fill="var(--brand-blue)"/>
    </svg>
    <p class="tagline-back">we save your money</p>
  </section>
</main>
</body>
</html>
```